Clean & Inspiring Web Design Project

Quillstone Makers, LLC (also known as Q9-Makers) is a company which provides 3D printing services and products. The emphasis is on making these products and services available to the mass-market - customers and users who may or may not have prior experience with 3D printing and/or rapid prototyping technologies. We are a start-up company, looking to build a clean and creativity inspiring brand - our site must encourage visitor to engage and make something. Our aim is to help take mere ideas and turn them into tangible items. We want to show a fusion of ideas (e.g. pencil sketches on graph paper) with design tools (e.g. CAD and drafting software) and rapid prototyping (e.g. TurnKit 3D printers, Stereolithography Machines, etc.). We would like the website to appear professional but at the same time easy to navigate and a good balance between text and pictures. The final design should inspire customers to nurture their ideas into real products and communicate our services to our customers. Our site should have the feel of a vibrant social community with the added benefit of tangible physical creations.

Target Market(s)

People with great ideas that need to be designed into a real product

Industry/Entity Type

Printing

Requirements
Must have
• - Website design should include 2 layouts - one for a "landing page" and one for a "content page"
- Website design must incorporate attached company logo (or derivative of this logo)
- Website design should incorporate the menu options shown in the attached PDF UI concept (UI does not necessarily need to look like the provided concept, just include all the clickable elements)
- Website design must portray an innovative and cooperative design environment with a look-and-feel that appeals to both amateur and professional designers.
- Please include pictures, illustrations and photographs (as needed) related to 3D printing, CAD design, conventional drafting, engineering and manufacturing industries.
- Design should support scaling to multiple screen sizes, from tablet computers (e.g. eSlate) to very large screen PCs.
- Design should include Username & Password fields for login or a button to pull up a login popup.
Nice to have
• - Website design could include "Invent", "Make", "Produce" and "Buy" options that slowly cycle through - with appropriate photos / graphics. These "menu options" would also be mouse-over enabled to switch into the appropriate context as the cursor enters that region (e.g. mouse over the "Invent" text would bring up page 2, etc.). (See attached Original UI Thoughts)
Should not have
• Requirements - Should Not Have:
- Website design should not portray a service that is very expensive or complicated - we are a reasonably priced service meant to be friendly with amateur inventors
- Website design should not be overly complicated - please keep it reasonably simple
- Website design should not be overly trendy
- Website design should not use more than 2 font styles, gaudy fonts, etc.
- Website design should not be "campy" or "tacky" - playful is ok, but please keep it elegant
- Website design should not be overly masculine or feminine - we will have both women and men as customers

```html
<!DOCTYPE html>
<html lang="en">
<head>
<meta charset="utf-8">
<title>Quillstone Makers, LLC</title>
<link rel="stylesheet" href="https://fonts.googleapis.com/css2?family=Oswald:wght@300;400;500;700&family=Arimo:ital,wght@0,400;0,700;1,400&display=swap">
<style>
  :root {
    --backdrop: #4b4b4b;
    --header: #98b6d8;
    --header-edge: #b9cfe8;
    --brand-blue: #1e5a96;
    --nav-blue: #1e4f8a;
    --title-navy: #1c3e6e;
    --idea-orange: #e08a10;
    --cart-blue: #1a9ed8;
    --frame: #9a9ca4;
    --button: #134c8a;
    --green: #1a9a1a;
    --cyan: #00d8c8;
    --navy: #1f2a8a;
    --magenta: #e010e0;
    --menu: #3a85c4;
    --menu-active: #1565a8;
    --footer: #262833;
    --white: #ffffff;
    --ink: #222222;
    --body-ink: #555555;
  }
  * { margin: 0; padding: 0; box-sizing: border-box; }
  html, body { width: 1200px; height: 1000px; overflow: hidden; }
  body { background: var(--backdrop); font-family: "Arimo", Arial, sans-serif; position: relative; }
  .page { position: absolute; left: 0; top: 211px; width: 1200px; height: 579px; box-shadow: 0 6px 10px rgba(0,0,0,.45); }
  .site-header { position: absolute; left: 0; top: 0; width: 1200px; height: 88px; background: var(--header); border-top: 1px solid var(--header-edge); border-bottom: 1px solid var(--header-edge); z-index: 2; box-shadow: 0 2px 4px rgba(0,0,0,.25); }
  .brand-mark { position: absolute; left: 310px; top: 6px; width: 44px; height: 44px; background: var(--brand-blue); border-radius: 3px; }
  .brand-name { position: absolute; left: 255px; top: 64px; font-size: 15px; color: var(--brand-blue); white-space: nowrap; }
  .tagline { position: absolute; left: 0; width: 1194px; top: 20px; text-align: center; font-family: "Oswald", sans-serif; font-size: 23px; color: var(--white); }
  .util-links { position: absolute; right: 258px; top: 9px; font-size: 8px; color: var(--nav-blue); }
  .cart { position: absolute; left: 890px; top: 33px; display: flex; align-items: center; gap: 3px; }
  .cart-count { width: 18px; height: 15px; background: var(--cart-blue); color: var(--white); font-size: 9px; text-align: center; line-height: 15px; }
  .main-nav { position: absolute; right: 258px; top: 72px; font-size: 9px; color: var(--nav-blue); word-spacing: 4px; white-space: nowrap; }
  .hero { position: absolute; left: 0; top: 88px; width: 1200px; height: 431px; background: linear-gradient(180deg, #bfe3f3 0%, #d6eef8 50%, #f3f9fb 78%, #ffffff 90%); }
  .social { position: absolute; left: 877px; top: 12px; display: flex; gap: 7px; }
  .social span { width: 17px; height: 17px; border-radius: 2px; background: #5b82b8; }
  .promo-title { position: absolute; left: 443px; top: 28px; font-family: "Oswald", sans-serif; font-weight: 500; font-size: 23px; line-height: 26px; color: var(--title-navy); }
  .promo-title em { font-style: normal; color: var(--idea-orange); }
  .promo-title sup { font-size: 12px; }
  .promo-art { position: absolute; left: 615px; top: 8px; width: 130px; height: 84px; border-radius: 20px; background: radial-gradient(circle at 40% 50%, #3a7fe0, #1e4fb0 60%, rgba(60,150,230,0) 100%); }
  .slider { position: absolute; left: 359px; top: 93px; width: 482px; height: 229px; background: var(--frame); border-radius: 6px; padding: 7px; }
  .slide { position: relative; width: 468px; height: 214px; background: var(--white); overflow: hidden; }
  .slide-photo { position: absolute; left: 150px; top: 0; width: 318px; height: 214px; background: linear-gradient(90deg, rgba(255,255,255,0) 0%, #f0a040 22%, #e8861a 45%, #e07c10 100%); }
  .slide-copy { position: absolute; left: 30px; top: 22px; width: 180px; }
  .slide-copy h2 { font-family: "Oswald", sans-serif; font-weight: 500; font-size: 24px; color: var(--ink); line-height: 28px; }
  .slide-copy h3 { font-family: "Oswald", sans-serif; font-weight: 300; font-size: 15px; color: var(--ink); margin-top: 2px; }
  .slide-copy p { font-size: 7.5px; line-height: 9.6px; color: var(--body-ink); margin-top: 9px; }
  .read-more { position: absolute; left: 30px; top: 168px; width: 66px; height: 23px; background: linear-gradient(#2a6aaa, var(--button)); border-radius: 4px; color: var(--white); font-size: 8px; font-style: italic; text-align: center; line-height: 23px; }
  .dots { position: absolute; left: 781px; top: 327px; display: flex; gap: 5px; }
  .dots span { width: 11px; height: 11px; border-radius: 50%; background: #cfd1d6; }
  .dots .active { background: #9a9ca4; }
  .callout { position: absolute; left: 257px; top: 474px; width: 172px; height: 45px; background: var(--green); color: var(--white); text-align: center; }
  .callout strong { display: block; font-family: "Oswald", sans-serif; font-weight: 500; font-size: 16px; line-height: 18px; margin-top: 5px; }
  .callout small { font-size: 8.5px; }
  .strip { position: absolute; top: 511px; height: 8px; width: 172px; }
  .strip.make { left: 429px; background: var(--cyan); }
  .strip.produce { left: 600px; width: 172px; background: var(--navy); }
  .strip.buy { left: 772px; background: var(--magenta); }
  .stages { position: absolute; left: 0; top: 519px; width: 1200px; height: 42px; background: var(--menu); }
  .stage { position: absolute; top: 0; width: 172px; height: 42px; font-family: "Oswald", sans-serif; font-size: 23px; color: var(--white); text-align: center; line-height: 42px; }
  .stage.active { background: var(--menu-active); }
  .site-footer { position: absolute; left: 0; top: 561px; width: 1200px; height: 18px; background: var(--footer); color: var(--white); font-size: 7.5px; }
  .copyright { position: absolute; left: 256px; top: 3px; }
  .footer-nav { position: absolute; right: 258px; top: 5px; word-spacing: 3px; }
</style>
</head>
<body>
<div class="page">
  <header class="site-header">
    <span class="brand-mark"></span>
    <div class="brand-name">Quillstone Makers, LLC®</div>
    <div class="tagline">Bringing Your Ideas to Market®</div>
    <div class="util-links">Help &nbsp;|&nbsp; FAQ</div>
    <div class="cart">
      <svg width="20" height="16" viewBox="0 0 20 16" aria-label="Cart"><path d="M1 2h3l2 9h10l2-7H5" fill="none" stroke="#1e3b5e" stroke-width="2"/><circle cx="8" cy="14" r="1.6" fill="#1e3b5e"/><circle cx="15" cy="14" r="1.6" fill="#1e3b5e"/></svg>
      <span class="cart-count">0</span>
      <svg width="9" height="8" viewBox="0 0 9 8"><path d="M1 2l3.5 4L8 2" fill="none" stroke="#1a9ed8" stroke-width="2"/></svg>
    </div>
    <nav class="main-nav">WHY Q9 &nbsp; | &nbsp; DREAMER &nbsp; | &nbsp; MAKER &nbsp; | &nbsp; PRODUCER</nav>
  </header>

  <section class="hero" role="img" aria-label="Soft sky with clouds">
    <div class="social"><span></span><span></span><span></span></div>
    <h1 class="promo-title">Give your <em>idea</em> the<br>3<sup>rd</sup> dimension</h1>
    <div class="promo-art" role="img" aria-label="Blue 3D lettering beside a small cartoon mascot"></div>
    <div class="slider">
      <div class="slide">
        <div class="slide-photo" role="img" aria-label="3D printed white parts and a ruler on an orange surface"></div>
        <div class="slide-copy">
          <h2>LOREM IPSUM</h2>
          <h3>Lorem ipsum</h3>
          <p>This is Sketchpad's version of Lorem Ipsum. Proin gravida nibh vel velit auctor aliquet. Aenean sollicitudin, lorem quis bibendum auctor, nisi elit consequat ipsum, nec sagittis sem nibh id elit. Duis sed odio sit amet nibh vulputate cursus a sit amet mauris. Morbi accumsan ipsum velit. Nam nec tellus a odio tincidunt auctor a ornare odio.</p>
        </div>
        <div class="read-more">Read more</div>
      </div>
    </div>
    <div class="dots"><span></span><span class="active"></span><span></span><span></span></div>
  </section>

  <div class="callout"><strong>Have an idea?</strong><small>We can make it real!</small></div>
  <span class="strip make"></span><span class="strip produce"></span><span class="strip buy"></span>

  <nav class="stages">
    <span class="stage active" style="left:257px">INVENT</span>
    <span class="stage" style="left:429px">Make</span>
    <span class="stage" style="left:600px">Produce</span>
    <span class="stage" style="left:772px">Buy</span>
  </nav>

  <footer class="site-footer">
    <span class="copyright">© 2012, Quillstone Makers, LLC</span>
    <span class="footer-nav">HOME &nbsp;| &nbsp;CONTACT &nbsp;| &nbsp;FRANCHISE &nbsp;| &nbsp;DISTRIBUTORS &nbsp;| &nbsp;CART</span>
  </footer>
</div>
</body>
</html>
```